Business Card Design - Law Firm

We are a boutique law firm located near the beach in Manly, Australia. We have recently had a new logo designed and are revamping our business cards with the new logo.

We have recently had a business card design done for us but are not entirely happy with it. We are looking for something modern, simplistic but striking. We would like to see multiple designs.

We have attached a word document which includes our new logo and the current business card design which we are looking at moving away from.

We would like the business cards to be double sided. We would like the design to include something which we can print in gloss colour when we send it to the business card printers.

```html
<!DOCTYPE html>
<html lang="en">
<head>
<meta charset="utf-8">
<title>Harlow &amp; Partners Lawyers – Business Card</title>
<link href="https://fonts.googleapis.com/css2?family=Montserrat:wght@400;500;700&display=swap" rel="stylesheet">
<style>
  :root {
    --stage: #2b2b2d;
    --navy: #34428f;
    --navy-mid: #4a5aa8;
    --navy-light: #7189c8;
    --ink: #1f1f24;
    --paper: #ffffff;
    --white: #ffffff;
  }
  * { box-sizing: border-box; margin: 0; padding: 0; }
  html, body {
    width: 1200px; height: 1200px; overflow: hidden;
    background: var(--stage);
    font-family: "Montserrat", Arial, sans-serif;
  }
  .stage {
    width: 1200px; height: 1200px;
    display: flex; flex-direction: column; align-items: center; justify-content: center;
    gap: 60px;
  }
  .card {
    width: 840px; height: 480px;
    position: relative;
    box-shadow: 0 18px 40px rgba(0,0,0,.45);
  }
  /* Front */
  .card-front {
    background: linear-gradient(100deg, var(--navy) 0%, var(--navy-mid) 55%, var(--navy-light) 100%);
    display: flex; align-items: center; justify-content: center;
  }
  .card-front .wordmark {
    color: var(--white);
    text-align: center;
    font-weight: 700;
    font-size: 44px;
    letter-spacing: 4px;
    line-height: 1.25;
  }
  .wordmark .subline { font-size: 22px; letter-spacing: 16px; padding-left: 16px; }

  /* Back */
  .card-back {
    background: var(--paper);
    display: flex; align-items: center;
    padding: 0 56px;
  }
  .brand {
    width: 340px;
    display: flex; flex-direction: column; align-items: center; gap: 22px;
  }
  .brand-dot {
    width: 64px; height: 64px; border-radius: 50%;
    background: var(--navy);
  }
  .brand .wordmark {
    color: var(--ink);
    font-weight: 700;
    font-size: 30px;
    letter-spacing: 2px;
    text-align: center;
    line-height: 1.3;
  }
  .brand .wordmark .subline { font-size: 16px; letter-spacing: 11px; padding-left: 11px; }
  .divider {
    width: 2px; height: 260px; background: var(--navy);
    margin: 0 40px 0 28px;
  }
  .details { color: var(--ink); }
  .person-name {
    color: var(--navy); font-weight: 700; font-size: 30px; line-height: 1.1;
  }
  .person-role { font-size: 20px; font-weight: 500; margin-bottom: 22px; }
  .contact-list { list-style: none; display: flex; flex-direction: column; gap: 8px; margin-bottom: 24px; }
  .contact-list li { display: flex; align-items: center; gap: 12px; font-size: 18px; font-weight: 500; }
  .contact-list svg { width: 18px; height: 18px; flex: none; fill: var(--navy); }
  .address { font-size: 19px; font-weight: 500; line-height: 1.35; }
</style>
</head>
<body>
<main class="stage">
  <section class="card card-front" aria-label="Business card front">
    <div class="wordmark">Harlow &amp; Partners<br><span class="subline">LAWYERS</span></div>
  </section>

  <section class="card card-back" aria-label="Business card back">
    <div class="brand">
      <span class="brand-dot" aria-hidden="true"></span>
      <div class="wordmark">Harlow &amp; Partners<br><span class="subline">LAWYERS</span></div>
    </div>
    <span class="divider" aria-hidden="true"></span>
    <div class="details">
      <h1 class="person-name">Maya Ellison</h1>
      <p class="person-role">Practice Manager</p>
      <ul class="contact-list">
        <li>
          <svg viewBox="0 0 24 24" aria-hidden="true"><path d="M6.6 10.8a15.1 15.1 0 0 0 6.6 6.6l2.2-2.2a1 1 0 0 1 1-.25 11.4 11.4 0 0 0 3.6.57 1 1 0 0 1 1 1V20a1 1 0 0 1-1 1A17 17 0 0 1 3 4a1 1 0 0 1 1-1h3.5a1 1 0 0 1 1 1c0 1.25.2 2.45.57 3.57a1 1 0 0 1-.25 1z"/></svg>
          (02) 5550 1234
        </li>
        <li>
          <svg viewBox="0 0 24 24" aria-hidden="true"><path d="M2 5h20v14H2z M4 7l8 6 8-6" fill="none" stroke="currentColor"/><path d="M2 5h20v14H2V5zm2 2.3V17h16V7.3l-8 5.9-8-5.9zM5.3 7l6.7 4.9L18.7 7H5.3z"/></svg>
          maya.ellison@harbourlaw.com.au
        </li>
        <li>
          <svg viewBox="0 0 24 24" aria-hidden="true"><path d="M12 2a10 10 0 1 0 0 20 10 10 0 0 0 0-20zm6.9 6h-3a15.6 15.6 0 0 0-1.4-3.9A8 8 0 0 1 18.9 8zM12 4a14 14 0 0 1 1.9 4h-3.8A14 14 0 0 1 12 4zM4.3 14a8 8 0 0 1 0-4h3.4a16.5 16.5 0 0 0 0 4zm.8 2h3a15.6 15.6 0 0 0 1.4 3.9A8 8 0 0 1 5.1 16zm3-8h-3a8 8 0 0 1 4.3-3.9A15.6 15.6 0 0 0 8.1 8zM12 20a14 14 0 0 1-1.9-4h3.8A14 14 0 0 1 12 20zm2.3-6H9.7a14.7 14.7 0 0 1 0-4h4.6a14.7 14.7 0 0 1 0 4zm.3 5.9a15.6 15.6 0 0 0 1.4-3.9h3a8 8 0 0 1-4.4 3.9zM16.3 14a16.5 16.5 0 0 0 0-4h3.4a8 8 0 0 1 0 4z"/></svg>
          www.harlowandpartners.com.au
        </li>
      </ul>
      <p class="address">Suite 4, 12 Cove Street<br>SEAVIEW NSW 2000</p>
    </div>
  </section>
</main>
</body>
</html>
```